Brantley Oakhollow LLC. custom built/handcrafted

I am recent small business owner looking to sell my art(drawings) and woodworking projects from my home. I have a very rough draft of a simple card design created on a simple digital program. I was hoping for a fancier lettering on the initial letters (BO). More of a calligraphy style. Also, the yellow border around the logo I would like to be a gold foil look. For it to be shiny or reflective look and to keep the other letters black with a consistent font on the card and the card white.

Target Market(s)

Local and neighboring cities

Industry/Entity Type

Art (drawing)/Woodworking

Contact Information for Business Card

My email rpoakhollow@mailbright.net, phone number 617-530-4168. In the files provided it has a yellow border around the logo and I was looking to make that a gold foil.

Font styles to use
Serif
Decorative
Script

Requirements
Nice to have
• symbols for having a Facebook and Instagram

```html
<!DOCTYPE html>
<html lang="en">
<head>
<meta charset="utf-8">
<title>Brantley Oakhollow LLC. — Business Card</title>
<link rel="stylesheet" href="https://fonts.googleapis.com/css2?family=Marcellus&family=Josefin+Sans:wght@300;400&display=swap">
<style>
  :root {
    --backdrop: #d6d6d6;
    --card-white: #ffffff;
    --mustard: #e0b43a;
    --gold: #d9a82e;
    --ink: #141414;
    --rule: #3a3220;
  }
  * { box-sizing: border-box; margin: 0; padding: 0; }
  html, body {
    width: 1200px; height: 846px; overflow: hidden;
    background: var(--backdrop);
  }
  .canvas {
    position: relative; width: 1200px; height: 846px;
    display: flex; align-items: center; justify-content: center; gap: 40px;
  }
  .card {
    position: relative; width: 540px; height: 309px;
    box-shadow: 0 6px 18px rgba(0,0,0,0.18);
  }
  /* Front */
  .card--front { background: var(--card-white); }
  .front__frame {
    position: absolute; left: 60px; top: 30px; width: 420px; height: 210px;
    border: 2px solid var(--gold);
    display: flex; align-items: center; justify-content: center;
  }
  .front__name {
    font-family: "Marcellus", serif; font-size: 30px; letter-spacing: 0.06em;
    color: var(--ink); text-transform: uppercase; text-align: center; line-height: 1.2;
  }
  .front__tagline {
    position: absolute; right: 60px; top: 256px;
    font-family: "Marcellus", serif; font-size: 19px; letter-spacing: 0.08em;
    color: var(--ink); text-transform: uppercase;
  }
  /* Back */
  .card--back { background: var(--mustard); color: var(--ink); }
  .back__name {
    position: absolute; left: 0; right: 0; top: 58px; text-align: center;
    font-family: "Marcellus", serif; font-size: 36px; letter-spacing: 0.05em;
    text-transform: uppercase;
  }
  .back__role {
    position: absolute; left: 40px; right: 40px; top: 112px;
    display: flex; align-items: center; gap: 14px;
    font-family: "Marcellus", serif; font-size: 19px; letter-spacing: 0.08em;
    text-transform: uppercase;
  }
  .back__rule { flex: 1; height: 1px; background: var(--rule); }
  .contact {
    font-family: "Josefin Sans", sans-serif; font-weight: 400; font-size: 15px;
    list-style: none;
  }
  .contact li { display: flex; align-items: center; gap: 7px; margin-top: 7px; }
  .contact svg { width: 14px; height: 14px; flex: none; }
  .contact--direct { position: absolute; left: 36px; bottom: 28px; }
  .contact--social { position: absolute; right: 30px; top: 168px; }
  .social-mark { width: 14px; height: 14px; background: var(--ink); border-radius: 2px; flex: none; }
</style>
</head>
<body>
<main class="canvas">
  <section class="card card--front" aria-label="Card front">
    <div class="front__frame">
      <p class="front__name">Brantley<br>Oakhollow</p>
    </div>
    <p class="front__tagline">Custom Built • Handcrafted</p>
  </section>

  <section class="card card--back" aria-label="Card back">
    <h1 class="back__name">Rowan P. Oakhollow</h1>
    <div class="back__role">
      <span class="back__rule"></span>
      <span>Owner</span>
      <span class="back__rule"></span>
    </div>
    <ul class="contact contact--social">
      <li><span class="social-mark"></span>rpoakhollow@friendloop.net</li>
      <li><span class="social-mark"></span>rpoakhollow@snapfolio.net</li>
    </ul>
    <ul class="contact contact--direct">
      <li>
        <svg viewBox="0 0 24 24" aria-hidden="true"><path fill="#141414" d="M6.6 10.8a15 15 0 0 0 6.6 6.6l2.2-2.2a1 1 0 0 1 1-.25 11.4 11.4 0 0 0 3.6.57 1 1 0 0 1 1 1V20a1 1 0 0 1-1 1A17 17 0 0 1 3 4a1 1 0 0 1 1-1h3.5a1 1 0 0 1 1 1c0 1.25.2 2.45.57 3.6a1 1 0 0 1-.25 1z"/></svg>
        617-530-4168
      </li>
      <li>
        <svg viewBox="0 0 24 24" aria-hidden="true"><rect x="2" y="5" width="20" height="14" fill="#141414"/><path d="M2 5l10 8 10-8" fill="none" stroke="#e0b43a" stroke-width="1.6"/></svg>
        rpoakhollow@mailbright.net
      </li>
    </ul>
  </section>
</main>
</body>
</html>
```